Bref créative
Business Card for Education Consulting Company
Brio Study Mentors
Simple
Marcus Delavine
President
317 Hollins Court NE
Washington DC 20019
Marcus@briostudymentors-example.com
www.briostudymentors-example.com
Looking for a simple, clean and professional business card. The logo already has the name of the company so there is no need to include again unless you feel it adds to the overall look of the card.
Here is the compnay's logo

```html
<!DOCTYPE html>
<html lang="en">
<head>
<meta charset="utf-8">
<title>Brio Study Mentors – Business Card</title>
<link href="https://fonts.googleapis.com/css2?family=Tinos:wght@400;700&display=swap" rel="stylesheet">
<style>
  :root {
    --stage: #3a3d42;
    --card-light: #ffffff;
    --card-shade: #dfe1e4;
    --brand-blue: #1f5fae;
    --brand-blue-deep: #123f80;
    --brand-blue-bright: #3d86d8;
    --text-grey: #555a60;
    --swoosh-grey: #9aa0a8;
    --map-tone: #c9ccd1;
  }
  * { box-sizing: border-box; margin: 0; padding: 0; }
  html, body { width: 1200px; height: 901px; overflow: hidden; }
  body {
    background: var(--stage);
    font-family: "Tinos", "Times New Roman", serif;
    display: flex; align-items: center; justify-content: center; gap: 40px;
  }
  .card {
    position: relative; width: 520px; height: 297px;
    border-radius: 18px; overflow: hidden;
    background: linear-gradient(160deg, var(--card-light) 0%, #f1f2f4 55%, var(--card-shade) 100%);
  }
  /* back */
  .world-map {
    position: absolute; left: 40px; top: 20px; width: 440px; height: 257px;
    border-radius: 40% 50% 45% 40%;
    background: radial-gradient(ellipse at 50% 50%, var(--map-tone) 0%, rgba(201,204,209,0.4) 55%, rgba(201,204,209,0) 75%);
  }
  .back-brand {
    position: absolute; inset: 0; display: flex; align-items: center; justify-content: center; gap: 10px;
  }
  .brand-dot { width: 26px; height: 26px; border-radius: 50%; background: var(--brand-blue); flex: none; }
  .brand-name { color: var(--brand-blue); font-weight: 700; font-size: 34px; letter-spacing: 0.5px; }
  /* front */
  .front-brand { position: absolute; left: 26px; top: 78px; display: flex; align-items: center; gap: 8px; }
  .front-brand .brand-dot { width: 20px; height: 20px; }
  .front-brand .brand-name { font-size: 24px; line-height: 1.05; }
  .divider { position: absolute; left: 286px; top: 72px; width: 3px; height: 116px; background: var(--brand-blue); }
  .contact { position: absolute; left: 300px; top: 68px; color: var(--text-grey); font-size: 11.5px; line-height: 1.35; }
  .person-name { color: var(--brand-blue); font-weight: 700; font-size: 18px; }
  .person-role { font-size: 11.5px; margin-bottom: 16px; }
  .address { margin-bottom: 12px; }
  .contact-line { display: flex; align-items: center; gap: 6px; }
  .contact-line svg { width: 11px; height: 11px; flex: none; }
  .swoosh { position: absolute; left: 0; bottom: 0; width: 520px; height: 110px; }
  .website {
    position: absolute; left: 0; right: 0; bottom: 16px; text-align: center;
    color: #ffffff; font-size: 12px; letter-spacing: 3px;
  }
</style>
</head>
<body>
  <section class="card card-back">
    <div class="world-map" role="img" aria-label="Faint world map background"></div>
    <div class="back-brand">
      <span class="brand-dot"></span>
      <span class="brand-name">Brio Study Mentors</span>
    </div>
  </section>

  <section class="card card-front">
    <div class="front-brand">
      <span class="brand-dot"></span>
      <span class="brand-name">Brio Study<br>Mentors</span>
    </div>
    <div class="divider"></div>
    <div class="contact">
      <div class="person-name">Marcus Delavine</div>
      <div class="person-role">President</div>
      <div class="address">317 Hollins Court NE<br>Washington DC 20019</div>
      <div class="contact-line">
        <svg viewBox="0 0 12 12"><path d="M2 1h2.5l1 3-1.5 1a7 7 0 0 0 3 3l1-1.5 3 1V10a1 1 0 0 1-1 1A10 10 0 0 1 1 2a1 1 0 0 1 1-1z" fill="var(--brand-blue)"/></svg>
        <span>202-555-0147</span>
      </div>
      <div class="contact-line">
        <svg viewBox="0 0 12 12"><rect x="0.5" y="2" width="11" height="8" rx="1" fill="var(--brand-blue)"/><path d="M1 3l5 4 5-4" stroke="#fff" stroke-width="1" fill="none"/></svg>
        <span>Marcus@briostudymentors-example.com</span>
      </div>
    </div>
    <svg class="swoosh" viewBox="0 0 520 110" preserveAspectRatio="none" aria-hidden="true">
      <defs>
        <linearGradient id="blueBand" x1="0" y1="0" x2="1" y2="1">
          <stop offset="0" stop-color="var(--brand-blue-bright)"/>
          <stop offset="1" stop-color="var(--brand-blue-deep)"/>
        </linearGradient>
      </defs>
      <path d="M0 30 C150 0 330 10 520 40 L520 110 L0 110 Z" fill="url(#blueBand)"/>
      <path d="M0 58 C160 30 340 45 520 60 L520 68 C340 55 160 42 0 66 Z" fill="var(--swoosh-grey)"/>
      <path d="M0 66 C160 42 340 55 520 68" stroke="#ffffff" stroke-width="2" fill="none"/>
      <path d="M0 72 C170 52 350 64 520 78 L520 110 L0 110 Z" fill="url(#blueBand)"/>
    </svg>
    <div class="website">www.briostudymentors-example.com</div>
  </section>
</body>
</html>
```